New box design for our unique Do-it-Yourself Mushroom Log Kit and Oyster Mushroom Book Recycler Kit

We are looking for a stylish and eye catching design for our range of gourmet mushroom growing kits. The kits are aimed at the gift market and are bought for people who have an interest in growing their own gourmet food and with an interest in mushrooms and mushroom growing.

'Our range of DIY Mushroom Log Kits is attractively packaged containing everything needed to grow gourmet mushrooms using your own logs. With comprehensive, yet easy to follow instuctions, they are ideal for beginners and make interesting gifts and presents for all ages. Each mushroom species can be grown using a wide variety of tree species so the right type of log is easy to find. They are productive, great tasting, and the growing process is both fun and educational.' Three mushroom species: Shiitake, Chicken-of-the-woods, Pearl Oyster.
Webiste link: https://www.fernbrookfungi.co.uk/product-category/mushroom-log-kits/

The 'Oyster Mushroom Book Recyler Kit' is an indoor mushroom growing kit: 'A quick, fun, and easy introduction to gourmet mushroom growing and a novel gift idea too! Taking just twenty minutes to prepare and beginning to crop in as little as two weeks, three crops of oyster mushroom are possible. Once the kit has finished producing indoors, it can then be used to a make an outdoor mushroom bed. Full instructions are included for this nice little gourmet mushroom indoor growing kit.'
Web link: https://www.fernbrookfungi.co.uk/shop/oyster-mushroom-recycler-kits/gourmet-mushroom-indoor-growing-kit/

Box size: 170 mm x 100 mm x 80 mm
Colour scheme should reflect an ecological, natural theme with text areas for descriptions of the mushroom species and how the product works.

Target Market(s)

Gifts for Gardeners, Food Lovers, Home Growing, Mushroom Enthusiasts, Environmentalists, Ecology, Natural Food

Industry/Entity Type

Agriculture

Font styles to use
Decorative

Requirements
Must have
• Images of the mushrooms to be prominent. Inset images to provide backup for the products description and how to use the product.
• Box 1: Oyster Mushroom Book Recycler Kit
• Headline: 'A fun and easy way to grow Gourmet Mushrooms'
• Description:
• 'Turn an old book into a mini mushroom farm! Taking just twenty minutes to prepare and beginning to crop in as little as two weeks, three crops of oyster mushroom are possible. Once the kit has finished producing indoors, it can then be used to a make an outdoor mushroom bed. Full instructions are included'.
• Contents:
• 1 Packet of Oyster Mushroom Grain Spawn
• 1 Filter Grow Bag
• 3 Rubber Bands
• 1 Instruction Sheet
• Storage: Grain Spawn can be stored in the fridge for 3 months and is supplied with a Use-by-Date (see inside).
• Box 2: Shiitake DIY Mushroom Log Kit
• Headline: 'Grow Shiitake Mushrooms Naturally Using Your Own Log'
• Description:
• The quality of Shiitake mushrooms grown naturally using logs is much superior to shop bought mushrooms. They have a richer intense flavour, and a substantial firmer texture, giving the grower a truly authentic gourmet experience. Oak logs are ideal, producing a mushroom crop bi-annually for up to seven years. Other hardwood logs can be used as Shiitake is one of the easiest gourmet mushrooms to grow.
• Contents:
• Plug Spawn: 60 Plugs for 1 x 1m log or 2 x 50 cm logs
• 50g of Soya Wax to seal in the plugs
• 1 x Wax Application Brush
• 1 x 8mm Drill Bit
• Instruction Booklet
• Storage: Plug Spawn can be stored for up to 6 months in a fridge and is supplied with a Use-by-Date (see inside).
• Box 3: Pearl Oyster DIY Mushroom Log Kit
• Headline: 'Grow Pearl Oyster Mushrooms Naturally Using Your Own Log'
• Description:
• Pearl Oyster mushroom is a versatile and productive species making it ideal for beginners. Commonly known as the ‘Tree Oyster’ - a long time favourite of wild mushroom hunters - this winter loving oyster mushroom is easy to grow and delicious to eat, on account of it’s unusually thick and fleshy cap. Great in stir-fries, as a gourmet mushroom pizza topping, or in an oyster mushroom and ale pie.
• Contents:
• 1 x 8mm Drill Bit
• Instruction Booklet
• Box 4: Chicken-of-the-Woods DIY Mushroom Log Kit
• Headline: 'Grow Chicken-of-the-Woods Naturally Using Your Own Log'
• Description:
• Chicken-of-the-woods is an exciting find on summer wild mushroom forays, where it usually found on dead and dying trees. As its name suggests the taste and texture strongly resembles poultry meat, making for a very interesting culinary experience—especially for vegetarians. It can easily be grown using a wide variety of hardwood logs and tree stumps.
• Contents:
• Plug Spawn: 60 Plugs for 1 x 1m log
• 1 x 8mm Drill Bit
• Instruction Booklet
Nice to have
• To be honest, I am not very good at design, so I am for looking for some creative help here, so please feel free to do so. As long as the design is clean, and nicely laid out with attractive fonts, that is my main aim for the product.

```html
<!DOCTYPE html>
<html lang="en">
<head>
<meta charset="utf-8">
<title>Oyster Mushroom Book Recycler Kit – Box Panels</title>
<link rel="stylesheet" href="https://fonts.googleapis.com/css2?family=Open+Sans:wght@400;600;700;800&display=swap">
<style>
  :root {
    --stage: #ececec;
    --kraft: #c8a26b;
    --kraft-light: #d3b07a;
    --kraft-dark: #b8915b;
    --leaf: #7cc242;
    --leaf-deep: #6aae34;
    --bark: #6e4a22;
    --slate: #2e3947;
    --mushroom: #d9c8ad;
    --mushroom-shade: #a89579;
    --bag: #3a3a3a;
    --fold: rgba(60, 40, 20, 0.35);
  }
  * { box-sizing: border-box; margin: 0; padding: 0; }
  html, body {
    width: 1200px; height: 960px; overflow: hidden;
    background: var(--stage);
    font-family: "Open Sans", sans-serif;
  }
  .canvas { position: relative; width: 1200px; height: 960px; }

  .panel {
    position: absolute;
    background:
      radial-gradient(circle at 30% 40%, var(--kraft-light), transparent 60%),
      radial-gradient(circle at 80% 70%, var(--kraft-dark), transparent 55%),
      var(--kraft);
    outline: 1px dashed var(--fold);
    overflow: hidden;
  }
  .panel--top   { left: 485px; top: 183px; width: 560px; height: 330px; }
  .panel--front { left: 485px; top: 513px; width: 560px; height: 264px; }
  .panel--side  { left: 155px; top: 513px; width: 330px; height: 264px; }

  .splash {
    position: absolute;
    background: var(--leaf);
    border-radius: 46% 54% 40% 60% / 55% 45% 55% 45%;
  }
  .photo { position: absolute; border-radius: 10px; }
  .photo--cluster {
    background: radial-gradient(ellipse at 50% 40%, var(--mushroom), var(--mushroom-shade) 80%);
    border-radius: 45% 45% 30% 30%;
  }
  .photo--bag {
    background: linear-gradient(180deg, var(--mushroom) 0 32%, var(--bag) 32% 100%);
    border-radius: 8px;
  }

  .title {
    color: var(--bark);
    font-weight: 800;
    line-height: 1.02;
  }
  .subtitle { color: var(--slate); font-weight: 700; line-height: 1.1; }
  .tagline  { color: var(--slate); font-weight: 600; line-height: 1.2; }

  /* top panel */
  .panel--top .splash { left: -30px; top: -30px; width: 300px; height: 250px; border-radius: 0 60% 55% 10% / 0 50% 60% 20%; }
  .panel--top .photo--bag { left: 30px; top: 40px; width: 200px; height: 150px; }
  .panel--top .copy { position: absolute; left: 265px; top: 40px; width: 280px; }
  .panel--top .title { font-size: 40px; }
  .panel--top .subtitle { font-size: 26px; margin-top: 6px; }
  .panel--top .tagline { font-size: 17px; margin-top: 8px; }

  /* front panel */
  .panel--front .splash { left: 360px; top: 30px; width: 220px; height: 200px; }
  .panel--front .photo--cluster { left: 370px; top: 34px; width: 180px; height: 190px; }
  .panel--front .copy { position: absolute; left: 36px; top: 30px; width: 340px; }
  .panel--front .title { font-size: 46px; }
  .panel--front .subtitle { font-size: 30px; margin-top: 6px; }
  .panel--front .tagline { font-size: 21px; margin-top: 12px; }

  /* side panel */
  .panel--side .splash { left: 6px; top: 20px; width: 130px; height: 226px; }
  .panel--side .photo--bag { left: 26px; top: 30px; width: 92px; height: 200px; }
  .contents { position: absolute; left: 150px; top: 36px; width: 170px; }
  .contents__heading { color: var(--slate); font-weight: 700; font-size: 22px; margin-bottom: 8px; }
  .contents__list { list-style: none; }
  .contents__item {
    display: flex; gap: 5px;
    color: var(--slate); font-size: 11px; line-height: 1.3; margin-bottom: 4px;
  }
  .contents__item svg { flex: none; margin-top: 3px; }
</style>
</head>
<body>
<main class="canvas">

  <section class="panel panel--top" aria-label="Box lid">
    <div class="splash"></div>
    <div class="photo photo--bag" role="img" aria-label="Photo of oyster mushrooms growing from a filter bag"></div>
    <div class="copy">
      <h2 class="title">Oyster Mushroom</h2>
      <p class="subtitle">Book Recycler Kit</p>
      <p class="tagline">A fun and easy way to grow oyster mushrooms</p>
    </div>
  </section>

  <section class="panel panel--side" aria-label="Box side">
    <div class="splash"></div>
    <div class="photo photo--bag" role="img" aria-label="Photo of oyster mushrooms sprouting from a grow bag"></div>
    <div class="contents">
      <h3 class="contents__heading">Kit includes</h3>
      <ul class="contents__list">
        <li class="contents__item"><svg width="8" height="8" viewBox="0 0 8 8"><path d="M1 4.5 3 6.5 7 1.5" fill="none" stroke="currentColor" stroke-width="1.3"/></svg>1 bag of oyster mushroom grain spawn</li>
        <li class="contents__item"><svg width="8" height="8" viewBox="0 0 8 8"><path d="M1 4.5 3 6.5 7 1.5" fill="none" stroke="currentColor" stroke-width="1.3"/></svg>Willowtex Filter Bag</li>
        <li class="contents__item"><svg width="8" height="8" viewBox="0 0 8 8"><path d="M1 4.5 3 6.5 7 1.5" fill="none" stroke="currentColor" stroke-width="1.3"/></svg>3 rubber bands</li>
        <li class="contents__item"><svg width="8" height="8" viewBox="0 0 8 8"><path d="M1 4.5 3 6.5 7 1.5" fill="none" stroke="currentColor" stroke-width="1.3"/></svg>Instruction sheet</li>
        <li class="contents__item"><svg width="8" height="8" viewBox="0 0 8 8"><path d="M1 4.5 3 6.5 7 1.5" fill="none" stroke="currentColor" stroke-width="1.3"/></svg>Grain Spawn can be stored in the fridge for 3 months</li>
      </ul>
    </div>
  </section>

  <section class="panel panel--front" aria-label="Box front">
    <div class="splash"></div>
    <div class="photo photo--cluster" role="img" aria-label="Photo of a cluster of pale oyster mushrooms"></div>
    <div class="copy">
      <h1 class="title">Oyster<br>Mushroom</h1>
      <p class="subtitle">Book Recycler Kit</p>
      <p class="tagline">A fun and easy way to<br>grow oyster mushrooms</p>
    </div>
  </section>

</main>
</body>
</html>
```